Business Card Design for ClearPathVitality

We need the new logo on a business card for 3 employees:
Nora Kettering, PhD, Advanced Instructor and Practitioner of SomaLink Integral Medicine (email: nora@clearpathvitality.com)
Ray Holm, Business Manager (email: ray@clearpathvitality.com)
Bea Marlowe, Administrative Assistant (email: bea@quillowmere.com)

Target Market(s)

healthcare professionals

Industry/Entity Type

Alternative Medicine

Contact Information for Business Card

Names, titles, emails (names, titles, emails are in project description), phone, address, website, with logo and tagline. See below for address, phone, website: 418 Alder Ln, Bldg 12, Ste 305
Larkfield Cove, CA 94987
831-555-2746
www.clearpathvitality.com
Tagline: Roots of Balance, Light of Renewal

Font styles to use
Other font styles liked:
• Gabriela

Colors
00a990
86cfc6
6b449b
b7a5cd
85abd2
abd036

Requirements
Must have
• Colors and style that match the logo design - shades such as blue, green, purple
• Compatible or same font as in the logo
Nice to have
• Nice if it goes with the theme of Nora's last business card - uploaded below
Should not have
• colors or style in conflict with the logo

```html
<!DOCTYPE html>
<html lang="en">
<head>
<meta charset="utf-8">
<title>ClearPathVitality Business Cards</title>
<link href="https://fonts.googleapis.com/css2?family=Montserrat:wght@400;500&display=swap" rel="stylesheet">
<style>
  :root {
    --bg: #ecebe8;
    --back-top: #0a78c4;
    --back-bottom: #3f4a9e;
    --white: #ffffff;
    --name-blue: #1a7fc4;
    --ink: #3a3a3a;
    --purple: #4a2a82;
    --green-light: #8cc63f;
    --green-deep: #22b35a;
  }
  * { box-sizing: border-box; margin: 0; padding: 0; }
  html, body { width: 1200px; height: 930px; overflow: hidden; }
  body {
    background: var(--bg);
    font-family: "Montserrat", sans-serif;
    position: relative;
  }
  .card {
    position: absolute;
    width: 560px;
    height: 320px;
    border-radius: 14px;
    overflow: hidden;
    box-shadow: 0 10px 28px rgba(0,0,0,0.18);
  }
  /* Back of card */
  .card-back {
    left: 70px;
    top: 80px;
    background: linear-gradient(225deg, var(--back-top) 0%, var(--back-bottom) 100%);
    color: var(--white);
  }
  .card-back .brand {
    position: absolute;
    left: 0; right: 0; top: 120px;
    display: flex;
    align-items: center;
    justify-content: center;
    gap: 18px;
  }
  .card-back .brand-dot {
    width: 54px; height: 54px;
    border-radius: 50%;
    border: 4px solid var(--white);
  }
  .card-back .brand-name {
    font-size: 36px;
    font-weight: 500;
    letter-spacing: 0.5px;
    color: var(--white);
  }
  .card-back .web {
    position: absolute;
    left: 0; right: 0; bottom: 44px;
    text-align: center;
    font-size: 14px;
    font-weight: 400;
    letter-spacing: 0.3px;
  }
  /* Front of card */
  .card-front {
    left: 570px;
    top: 520px;
    background: var(--white);
  }
  .card-front .decor {
    position: absolute;
    right: -130px;
    top: -150px;
    width: 360px;
    height: 360px;
  }
  .card-front .brand {
    position: absolute;
    left: 34px;
    top: 48px;
    display: flex;
    align-items: center;
    gap: 12px;
  }
  .card-front .brand-dot {
    width: 40px; height: 40px;
    border-radius: 50%;
    background: var(--purple);
  }
  .card-front .brand-name {
    font-size: 24px;
    font-weight: 500;
    color: var(--purple);
  }
  .person {
    position: absolute;
    left: 34px;
    top: 132px;
  }
  .person-name {
    font-size: 25px;
    font-weight: 400;
    color: var(--name-blue);
    line-height: 1.1;
  }
  .person-title {
    font-size: 12.5px;
    color: var(--ink);
    margin-top: 2px;
  }
  .address {
    margin-top: 12px;
    font-size: 12.5px;
    line-height: 1.4;
    color: var(--ink);
  }
  .contacts {
    list-style: none;
    margin-top: 8px;
    font-size: 12.5px;
    line-height: 1.45;
    color: var(--ink);
  }
  .contacts li { display: flex; align-items: center; gap: 8px; }
  .contacts svg { width: 11px; height: 11px; flex: none; }
</style>
</head>
<body>

  <section class="card card-back" aria-label="Business card back">
    <div class="brand">
      <span class="brand-dot"></span>
      <span class="brand-name">ClearPathVitality</span>
    </div>
    <p class="web">www.clearpathvitality.com</p>
  </section>

  <section class="card card-front" aria-label="Business card front">
    <svg class="decor" viewBox="0 0 360 360" role="img" aria-label="Large brand symbol decoration in green and purple">
      <defs>
        <linearGradient id="decor-fill" x1="0" y1="0" x2="1" y2="1">
          <stop offset="0" stop-color="#8cc63f"/>
          <stop offset="1" stop-color="#22b35a"/>
        </linearGradient>
      </defs>
      <circle cx="180" cy="180" r="178" fill="url(#decor-fill)"/>
    </svg>

    <div class="brand">
      <span class="brand-dot"></span>
      <span class="brand-name">ClearPathVitality</span>
    </div>

    <div class="person">
      <h1 class="person-name">Bea Marlowe</h1>
      <p class="person-title">Administrative Assistant</p>
      <p class="address">418 Alder Ln,<br>Bldg 12, Ste 305<br>Larkfield Cove, CA 94987</p>
      <ul class="contacts">
        <li>
          <svg viewBox="0 0 12 12" aria-hidden="true"><path d="M2.5 1h2l1 3-1.3 1a6 6 0 0 0 2.8 2.8L8 6.5l3 1v2c0 .8-.7 1.5-1.5 1.5A8.5 8.5 0 0 1 1 2.5C1 1.7 1.7 1 2.5 1z" fill="#1a7fc4"/></svg>
          831-555-2746
        </li>
        <li>
          <svg viewBox="0 0 12 12" aria-hidden="true"><rect x="1" y="2.5" width="10" height="7" rx="1" fill="none" stroke="#1a7fc4" stroke-width="1.2"/><path d="M1.5 3l4.5 3.5L10.5 3" fill="none" stroke="#1a7fc4" stroke-width="1.2"/></svg>
          bea@quillowmere.com
        </li>
        <li>
          <svg viewBox="0 0 12 12" aria-hidden="true"><circle cx="6" cy="6" r="5" fill="none" stroke="#1a7fc4" stroke-width="1.1"/><ellipse cx="6" cy="6" rx="2.2" ry="5" fill="none" stroke="#1a7fc4" stroke-width="1"/><path d="M1 6h10" stroke="#1a7fc4" stroke-width="1"/></svg>
          www.clearpathvitality.com
        </li>
      </ul>
    </div>
  </section>

</body>
</html>
```